Dulwick Medical

Need smart and sleek business cards design for my medical distribution company. use logos attached.

add my details

Harriet Colbeck
Director/Sales Agent
harriet@dulwickmedical.com.au
0461 835 207

```html
<!DOCTYPE html>
<html lang="en">
<head>
<meta charset="utf-8">
<title>Dulwick Medical – Business Cards</title>
<link rel="stylesheet" href="https://fonts.googleapis.com/css2?family=Montserrat:wght@400;500;700&display=swap">
<style>
  :root {
    --page-bg: #c4c4c4;
    --navy: #1c2a5e;
    --navy-deep: #16224f;
    --navy-light: #2a3a78;
    --accent: #2a8cc4;
    --white: #ffffff;
  }
  html, body {
    margin: 0;
    width: 1200px;
    height: 802px;
    overflow: hidden;
    background: var(--page-bg);
    font-family: "Montserrat", sans-serif;
  }
  .sheet {
    position: relative;
    width: 1200px;
    height: 802px;
    display: flex;
    align-items: center;
    justify-content: center;
    gap: 40px;
  }
  .card {
    position: relative;
    width: 540px;
    height: 309px;
    border-radius: 22px;
    overflow: hidden;
    box-shadow: 0 14px 30px rgba(0,0,0,0.28);
  }
  /* Front */
  .card--front { background: var(--white); }
  .card--front .wave { position: absolute; inset: 0; width: 100%; height: 100%; }
  .brand {
    position: absolute;
    display: flex;
    align-items: center;
    gap: 10px;
  }
  .brand__mark {
    width: 20px;
    height: 20px;
    background: var(--accent);
  }
  .brand__name {
    font-weight: 700;
    letter-spacing: 0.02em;
    text-transform: uppercase;
    line-height: 1;
    white-space: nowrap;
  }
  .card--front .brand { left: 36px; top: 130px; }
  .card--front .brand__name { color: var(--navy); font-size: 22px; }

  .contact {
    position: absolute;
    right: 30px;
    top: 184px;
    text-align: right;
    color: var(--white);
  }
  .contact__name {
    margin: 0;
    font-size: 18px;
    font-weight: 700;
    line-height: 1.2;
    color: var(--accent);
    text-transform: uppercase;
    letter-spacing: 0.01em;
  }
  .contact__title {
    margin: 3px 0 14px;
    font-size: 12px;
    font-weight: 400;
  }
  .contact__line {
    display: flex;
    justify-content: flex-end;
    align-items: center;
    gap: 8px;
    margin: 0 0 7px;
    font-size: 12px;
  }
  .contact__icon { width: 12px; height: 12px; fill: var(--accent); }

  /* Back */
  .card--back {
    background: linear-gradient(150deg, var(--navy-deep) 0%, var(--navy) 55%, var(--navy-light) 100%);
  }
  .card--back .backdrop {
    position: absolute; inset: 0;
    background: radial-gradient(circle at 80% 15%, rgba(120,140,200,0.28), transparent 55%);
  }
  .card--back .brand {
    left: 50%;
    top: 50%;
    transform: translate(-50%, -50%);
    gap: 12px;
  }
  .card--back .brand__mark { background: var(--white); width: 26px; height: 26px; }
  .card--back .brand__name { color: var(--white); font-size: 32px; }
</style>
</head>
<body>
<main class="sheet">
  <section class="card card--front" aria-label="Business card front">
    <svg class="wave" viewBox="0 0 540 309" preserveAspectRatio="none" aria-hidden="true">
      <path d="M0,232 C120,268 250,262 320,170 C370,100 440,76 540,74 L540,309 L0,309 Z" fill="var(--accent)"/>
      <path d="M0,240 C120,276 254,270 324,178 C374,108 442,84 540,82 L540,309 L0,309 Z" fill="var(--white)"/>
      <path d="M0,246 C120,282 258,276 328,184 C378,114 444,90 540,88 L540,309 L0,309 Z" fill="var(--navy)"/>
    </svg>
    <div class="brand">
      <span class="brand__mark"></span>
      <span class="brand__name">Dulwick Medical</span>
    </div>
    <div class="contact">
      <h1 class="contact__name">Harriet Colbeck</h1>
      <p class="contact__title">Director/Sales Agent</p>
      <p class="contact__line">0461 835 207
        <svg class="contact__icon" viewBox="0 0 24 24" aria-hidden="true"><path d="M6.6 10.8a15.1 15.1 0 0 0 6.6 6.6l2.2-2.2c.3-.3.7-.4 1-.2 1.1.4 2.3.6 3.6.6.6 0 1 .4 1 1V20c0 .6-.4 1-1 1C10.6 21 3 13.4 3 4c0-.6.4-1 1-1h3.5c.6 0 1 .4 1 1 0 1.3.2 2.5.6 3.6.1.3 0 .7-.2 1z"/></svg>
      </p>
      <p class="contact__line">harriet@dulwickmedical.com.au
        <svg class="contact__icon" viewBox="0 0 24 24" aria-hidden="true"><path d="M2 5h20v14H2z" fill="var(--accent)"/><path d="M3 6l9 7 9-7" fill="none" stroke="var(--navy)" stroke-width="2"/></svg>
      </p>
    </div>
  </section>

  <section class="card card--back" aria-label="Business card back">
    <div class="backdrop"></div>
    <div class="brand">
      <span class="brand__mark"></span>
      <span class="brand__name">Dulwick Medical</span>
    </div>
  </section>
</main>
</body>
</html>
```